We would like to design a logo, letter head, and business card.  

We have beauty colleges in the Kansas City Missouri USA area that have been around for 55 years.  We teach hair, skin and nail tech programs to students. Most of our students are female between the age of 18-30. 

Updates

• I appologize for failing to provide details on our addresses. We have 3 locations all with the same phone number.

Hall of Marquette 3140 NE County Rd 12 Blue Springs MO 64027

Hall of Marquette 4810 Pellham Kansas City MO 64125

Hall of Marquette 13460 Oak Hollow Blvd Grandview Mo 64138

Phone: (816) 555-0147

• Dale Marquette

President

3140 NE County Rd 12

Blue Springs MO 64027

(816) 555-0147

dale@trq-salonschool.com
Updates

Target Market(s)

18-30 Years Old

Industry/Entity Type

Business

Logo Text

Hall of Marquette Beauty College

Requirements
Must have
• Hall of Marquette Beauty College

```html
<!DOCTYPE html>
<html lang="en">
<head>
<meta charset="utf-8">
<title>Hall of Marquette Beauty College — Stationery</title>
<link rel="stylesheet" href="https://fonts.googleapis.com/css2?family=Oswald:wght@400;500&display=swap">
<style>
  :root {
    --brand-violet: #6200e0;
    --paper-lilac: #eee5f9;
    --sheet-edge: #8d84a0;
    --ink-grey: #66646b;
    --white: #ffffff;
  }
  * { box-sizing: border-box; margin: 0; padding: 0; }
  html, body {
    width: 1200px; height: 1039px; overflow: hidden;
    background: var(--white);
    font-family: "Oswald", "Arial Narrow", sans-serif;
  }
  .canvas { position: relative; width: 1200px; height: 1039px; }

  /* Wordmark: one colour, one weight */
  .wordmark {
    position: absolute;
    display: flex; flex-direction: column; align-items: center;
    color: var(--brand-violet);
    font-weight: 500;
    line-height: 1;
    white-space: nowrap;
  }
  .wordmark__name { letter-spacing: -0.01em; }
  .wordmark__sub { letter-spacing: 0.55em; margin-right: -0.55em; }

  .wordmark--master { left: 20px; top: 200px; width: 350px; }
  .wordmark--master .wordmark__name { font-size: 56px; }
  .wordmark--master .wordmark__sub { font-size: 19px; margin-top: 10px; }

  /* Business card */
  .business-card {
    position: absolute; left: 43px; top: 378px;
    width: 303px; height: 172px;
    background: var(--brand-violet);
    color: var(--white);
    text-align: center;
  }
  .wordmark--card { left: 0; right: 0; top: 20px; color: var(--white); }
  .wordmark--card .wordmark__name { font-size: 29px; }
  .wordmark--card .wordmark__sub { font-size: 9px; margin-top: 5px; }
  .card-person { position: absolute; left: 0; right: 0; top: 79px; }
  .card-person__name { font-size: 10.5px; font-weight: 500; letter-spacing: 0.03em; line-height: 1.2; }
  .card-person__role, .card-person__mobile { font-size: 7px; line-height: 1.5; letter-spacing: 0.02em; }
  .card-contact { position: absolute; left: 0; right: 0; top: 119px; font-size: 6.4px; font-weight: 500; line-height: 1.55; letter-spacing: 0.02em; }

  /* Letterhead */
  .letterhead {
    position: absolute; left: 425px; top: 22px;
    width: 711px; height: 1006px;
    background: var(--paper-lilac);
    border: 1px solid var(--sheet-edge);
  }
  .wordmark--letterhead { left: 0; right: 0; top: 48px; }
  .wordmark--letterhead .wordmark__name { font-size: 52px; }
  .wordmark--letterhead .wordmark__sub { font-size: 17px; margin-top: 9px; }
  .letterhead__rule {
    position: absolute; left: 68px; width: 578px; top: 932px;
    border-top: 1px solid var(--ink-grey);
  }
  .letterhead__footer {
    position: absolute; left: 0; right: 0; top: 944px;
    text-align: center; color: var(--ink-grey);
    font-size: 12.5px; line-height: 21px; letter-spacing: 0.05em;
  }
</style>
</head>
<body>
<main class="canvas">

  <div class="wordmark wordmark--master" aria-label="Hall of Marquette Beauty College">
    <span class="wordmark__name">Hall of Marquette</span>
    <span class="wordmark__sub">BEAUTY COLLEGE</span>
  </div>

  <section class="business-card" aria-label="Business card">
    <div class="wordmark wordmark--card">
      <span class="wordmark__name">Hall of Marquette</span>
      <span class="wordmark__sub">BEAUTY COLLEGE</span>
    </div>
    <div class="card-person">
      <p class="card-person__name">Mara Ellison</p>
      <p class="card-person__role">Director</p>
      <p class="card-person__mobile">Mobile&nbsp; +447700900418</p>
    </div>
    <div class="card-contact">
      <p>Hall of Marquette Beauty College</p>
      <p>Telephone 056010555219 Facsimile 056010555220</p>
      <p>Address 214 Ashcombe Road, Brindle, Kettleby, KB4 2TN, England</p>
      <p>Email mara@hmbc-school.com Website www.hallofmarquette-school.com</p>
    </div>
  </section>

  <section class="letterhead" aria-label="Letterhead">
    <div class="wordmark wordmark--letterhead">
      <span class="wordmark__name">Hall of Marquette</span>
      <span class="wordmark__sub">BEAUTY COLLEGE</span>
    </div>
    <div class="letterhead__rule"></div>
    <footer class="letterhead__footer">
      <p>Telephone 056010555219 Facsimile 056010555220 Address 214 Ashcombe Road, Brindle, Kettleby, KB4 2TN, England</p>
      <p>Email mara@hmbc-school.com Website www.hallofmarquette-school.com</p>
    </footer>
  </section>

</main>
</body>
</html>
```